Letterhead for New Orthopaedic Surgery Practice

My husband and I are starting our own practice named RB Spine & Vitality Center. We would like to create a nice simple but high class letterhead that doesn't use too much solid color ink when printing. I like the colors dark blue, gold, yellow. Open to other suggestions. We will need to list him and I both on the top of the letterhead. Here is the important information:
Lucinda Perrow, M.D. - Hand and Upper Extremity Surgery
Abena Quist, M.D. - Hip & Knee Replacement/General Orthopaedic Surgery
Location: 18735 North Harlow Pkwy
Maple Ridge, FL 33486
Phone: 954-218-4650
Fax: 954-582-1346
Email: info@myrbspine.com

The only thing is that the phone and fax numbers will change once we get into our space. I just want to get the design started. I am including several documents which are my previous practice letterhead, my current procedure room letterhead, and our new Logo. The other letterheads are just for examples but please think outside of the box! We would love to see some great designs.

Colors
0054AA
0677BA
7BADD7
CADEEF
E8F1F8
0094D4
00A9DD
6FCCEA
C7EBF8
E9F6FB

Requirements
Must have
• class, elegance, luxury

```html
<!DOCTYPE html>
<html lang="en">
<head>
<meta charset="utf-8">
<title>RB Spine &amp; Vitality Center — Letterhead</title>
<link rel="stylesheet" href="https://fonts.googleapis.com/css2?family=Lora:ital,wght@0,400;0,600;1,700&display=swap">
<style>
  :root {
    --navy: #1b2a57;
    --gold: #c4a05f;
    --paper: #ffffff;
    --backdrop: #7a7a7a;
  }
  html, body {
    margin: 0;
    padding: 0;
    width: 1200px;
    height: 1200px;
    overflow: hidden;
    background: var(--backdrop);
  }
  .letterhead {
    position: absolute;
    left: 228px;
    top: 72px;
    width: 745px;
    height: 1055px;
    background: var(--paper);
    overflow: hidden;
    font-family: "Lora", Georgia, serif;
    color: var(--navy);
  }
  .sheet-bands {
    position: absolute;
    inset: 0;
    width: 100%;
    height: 100%;
  }
  .brand-mark {
    position: absolute;
    left: 50px;
    top: 48px;
    width: 146px;
    height: 146px;
    border: 2px solid var(--gold);
    border-radius: 50%;
    box-sizing: border-box;
    display: flex;
    align-items: center;
    justify-content: center;
    text-align: center;
  }
  .brand-name {
    font-size: 16px;
    font-weight: 600;
    line-height: 1.25;
    letter-spacing: 0.04em;
    color: var(--navy);
    margin: 0;
  }
  .physicians {
    position: absolute;
    right: 35px;
    top: 72px;
    margin: 0;
    padding: 0;
    list-style: none;
    text-align: right;
    font-size: 12.5px;
    line-height: 15px;
  }
  .physician-name {
    font-style: italic;
    font-weight: 700;
  }
  .contact {
    position: absolute;
    right: 36px;
    top: 112px;
    margin: 0;
    padding: 0;
    list-style: none;
    font-size: 12.5px;
    line-height: 15px;
  }
  .contact-line {
    display: flex;
    justify-content: flex-end;
    align-items: center;
    gap: 8px;
  }
  .contact-icon {
    width: 8px;
    height: 8px;
    fill: var(--navy);
    flex: none;
  }
  .contact-spacer {
    width: 8px;
    flex: none;
  }
</style>
</head>
<body>
  <main class="letterhead">
    <svg class="sheet-bands" viewBox="0 0 596 844" preserveAspectRatio="none" aria-hidden="true">
      <path class="band-top-navy" fill="var(--navy)" d="M150,0 C250,30 400,38 596,34 L596,26 C400,31 250,24 160,0 Z"/>
      <path class="band-top-gold" fill="var(--gold)" d="M160,0 C250,24 400,31 596,26 L596,0 Z"/>
      <path class="band-bottom-navy" fill="var(--navy)" d="M0,798 C200,780 420,800 596,844 L596,844 C420,808 200,792 0,805 Z"/>
      <path class="band-bottom-gold" fill="var(--gold)" d="M0,805 C200,792 420,808 596,844 L0,844 Z"/>
    </svg>

    <div class="brand-mark">
      <p class="brand-name">RB Spine &amp;<br>Vitality<br>Center</p>
    </div>

    <ul class="physicians">
      <li><span class="physician-name">Lucinda Perrow</span>, M.D. - Hand and Upper Extremity Surgery</li>
      <li><span class="physician-name">Abena Quist</span>, M.D. - Hip &amp; Knee Replacement/General Orthopaedic Surgery</li>
    </ul>

    <ul class="contact">
      <li class="contact-line">18735 North Harlow Pkwy
        <svg class="contact-icon" viewBox="0 0 10 10" aria-label="Address"><path d="M5 0a3.5 3.5 0 0 0-3.5 3.5C1.5 6 5 10 5 10s3.5-4 3.5-6.5A3.5 3.5 0 0 0 5 0zm0 5a1.4 1.4 0 1 1 0-2.8A1.4 1.4 0 0 1 5 5z"/></svg>
      </li>
      <li class="contact-line">Maple Ridge, FL 33486 <span class="contact-spacer"></span></li>
      <li class="contact-line">954-218-4650
        <svg class="contact-icon" viewBox="0 0 10 10" aria-label="Phone"><path d="M2 0.5l1.6 2.2-1 1c.6 1.4 1.6 2.4 3 3l1-1L8.8 7.3 8 9.5C4 9.2.8 6 .5 2z"/></svg>
      </li>
      <li class="contact-line">954-582-1346
        <svg class="contact-icon" viewBox="0 0 10 10" aria-label="Fax"><path d="M2.5 0h5v3h-5zM0 3.5h10v4H8V10H2V7.5H0zM3 6v3h4V6z"/></svg>
      </li>
      <li class="contact-line">info@myrbspine.com
        <svg class="contact-icon" viewBox="0 0 10 10" aria-label="Email"><path d="M0 2h10v.8L5 5.6 0 2.8zM0 3.8l5 2.8 5-2.8V8H0z"/></svg>
      </li>
    </ul>
  </main>
</body>
</html>
```